Brim Chairworks Sales Brochure

We need a sales brochure designed made up of 12 pages. Our company supplies and installs Seating for various venues in Australia called 'Brim Chairworks'. We would like designs to showcase our products and projects. Our colours are Red, White and Black. These colours are not a must but would work well with our logo. Our Website is brimchairworks.com.au to get ideas. We will be using this brochure to help sell our seating products. I have provided the text in a word document and how I would the page layout with the photos to match the text.

```html
<!DOCTYPE html>
<html lang="en">
<head>
<meta charset="utf-8">
<title>Brim Chairworks Sales Brochure</title>
<link href="https://fonts.googleapis.com/css2?family=Montserrat:wght@400;500;600;700;800&display=swap" rel="stylesheet">
<style>
:root{
  --red:#e3202a;
  --black:#111111;
  --ink:#555555;
  --soft:#f3f3f3;
  --white:#ffffff;
  --line:#d8d8d8;
}
*{box-sizing:border-box;margin:0;padding:0}
html,body{width:1200px;height:3000px;overflow:hidden}
body{background:var(--white);font-family:'Montserrat',sans-serif;color:var(--ink);position:relative}
.page{position:absolute;width:330px;height:430px;background:var(--white);box-shadow:0 2px 10px rgba(0,0,0,.16);overflow:hidden}
.page.dark{background:var(--black)}
.section-head{position:relative;height:20px;margin:22px 0 12px 22px}
.section-head .band{display:block;width:max-content;background:var(--red);color:var(--white);font-weight:700;font-size:11.5px;line-height:20px;height:20px;padding:0 28px 0 10px;clip-path:polygon(0 0,88% 0,100% 100%,0 100%)}
.section-head::after{content:"";position:absolute;left:0;right:0;bottom:0;height:1.5px;background:var(--red)}
.photo{position:relative;overflow:hidden}
.tag{position:absolute;left:0;right:0;bottom:0;background:var(--red);color:var(--white);font-weight:600;font-size:7.5px;letter-spacing:.3px;padding:3px 8px;text-transform:uppercase;line-height:1.2}
.ph-red{background:linear-gradient(180deg,#3a0b0d 0%,#a1171d 45%,#d92a30 80%,#5a0e10 100%)}
.ph-court{background:linear-gradient(180deg,#2a2f38 0%,#6d7787 35%,#2f4f9a 60%,#c58c4f 80%,#e0ad6d 100%)}
.ph-blue{background:linear-gradient(160deg,#1c2350 0%,#3747a8 50%,#8a93d6 100%)}
.ph-dark{background:linear-gradient(180deg,#0e1118 0%,#2a3142 55%,#4b5366 100%)}
.ph-grey{background:linear-gradient(160deg,#e9e9e9 0%,#b8b8b8 60%,#7b7b7b 100%)}
.ph-mixed{background:linear-gradient(180deg,#d9dde3 0%,#8a2a30 55%,#c13038 75%,#3b3f48 100%)}
.ph-gold{background:linear-gradient(180deg,#1a1a1a 0%,#5a5a5a 40%,#d6a72a 70%,#333 100%)}
.ph-teal{background:linear-gradient(180deg,#181c22 0%,#365b4f 50%,#6a7d74 100%)}
.body-text{font-size:4.6px;line-height:1.45;color:var(--ink)}
.item-title{color:var(--red);font-weight:700;font-size:8.5px;text-transform:uppercase;margin-bottom:4px;line-height:1.15}
.rows{position:absolute;left:0;right:0;bottom:14px}
.row{display:flex;align-items:center;gap:14px;padding:0 22px 0 30px}
.row.shade{background:var(--soft)}
.row .photo{width:128px;flex:none}
.row .copy{flex:1}
.row .copy .body-text{border-bottom:1px dotted var(--line);padding-bottom:4px}

.brand{color:var(--white);font-weight:800;text-align:center;letter-spacing:1px}
.brand-mark{display:flex;align-items:center;justify-content:center;gap:8px}
.brand-dot{width:14px;height:14px;border-radius:50%;background:var(--red);flex:none}
.url-pill{position:absolute;left:82px;right:82px;bottom:26px;border:1.5px solid var(--white);border-radius:12px;color:var(--red);text-align:center;font-size:9.5px;line-height:20px}
.globe{position:absolute;left:50%;bottom:50px;transform:translateX(-50%)}

.about-block{padding:0 30px;margin-bottom:8px}
.about-block .section-head{margin:12px 0 6px 0;height:14px}
.about-block .section-head .band{font-size:8px;line-height:14px;height:14px;font-weight:500}

.grid2{position:absolute;left:30px;right:30px;display:grid;grid-template-columns:1fr 1fr;column-gap:18px}
.grid2 .cell .body-text{margin-top:4px;border-bottom:1px dotted var(--line);padding-bottom:4px}
.subhead{color:var(--black);font-size:7.5px;font-weight:600;text-transform:uppercase;margin:6px 0 4px}
.deck-name{color:var(--red);font-weight:700;font-size:5.5px;text-transform:uppercase;margin-top:3px}

.venues{position:absolute;left:30px;right:24px;top:38px}
.venue{display:flex;align-items:baseline;font-size:4.6px;line-height:13px;color:var(--red)}
.venue .name{width:88px;white-space:nowrap}
.venue .lead{width:30px;border-bottom:1px dotted #c9c9c9;margin:0 6px 0 2px}
.venue .qty{flex:1;white-space:nowrap}

.contact{position:absolute;left:0;right:0;text-align:center;color:var(--white)}
.dots{position:absolute;height:0;border-top:1px dotted #777;width:70px}
</style>
</head>
<body>

<section class="page dark" style="left:200px;top:50px">
  <div class="brand-mark" style="position:absolute;top:100px;left:0;right:0">
    <span class="brand-dot"></span>
    <span class="brand" style="font-size:22px">BRIM CHAIRWORKS</span>
  </div>
  <div class="photo" role="img" aria-label="Auditorium with rows of red theatre seats under stage lighting" style="position:absolute;left:0;right:0;top:200px;height:150px;background:linear-gradient(180deg,#111 0%,#3a0b0d 30%,#c4232a 70%,#2a0608 100%)"></div>
  <svg class="globe" width="12" height="12" viewBox="0 0 12 12"><circle cx="6" cy="6" r="5" fill="none" stroke="#fff" stroke-width="1"/><ellipse cx="6" cy="6" rx="2.2" ry="5" fill="none" stroke="#fff" stroke-width=".8"/><line x1="1" y1="6" x2="11" y2="6" stroke="#fff" stroke-width=".8"/></svg>
  <div class="url-pill">www.brimchairworks.com.au</div>
</section>

<section class="page" style="left:618px;top:50px">
  <div style="padding-top:20px">
    <div class="about-block">
      <div class="section-head"><span class="band">WHO WE ARE:</span></div>
      <p class="body-text">Brim Chairworks is an Australian owned and operated company with decades of combined experience in the sports and entertainment industry. We set the standard in Australia by delivering quality systems from trusted long established suppliers combined with outstanding customer service. We understand it is not just a product you are buying, so we offer a full service of design, quotation, installation and after-sales care.</p>
    </div>
    <div class="about-block">
      <div class="section-head"><span class="band">WHAT MAKES US DIFFERENT:</span></div>
      <p class="body-text">We provide a balanced approach to maximising your space and budget to ensure your audience is delivered a first class experience along with quality, code-compliant materials delivering longevity and value for money. We have a long standing commitment to safety and sustainability, and all equipment is built to last with warranties assured.</p>
    </div>
    <div class="about-block">
      <div class="section-head"><span class="band">SUPPLIERS:</span></div>
      <p class="body-text">Our platforms are supplied by Calder Seating Co, a family company with well over a century of experience. All platform manufacturing is done in house to the highest standard, and they designed one of the first telescopic platforms. Our most popular seat range is supplied by Northvale Seats, who have installed millions of seats across many countries, including some of the most prestigious stadiums and venues in the world.</p>
    </div>
  </div>
  <div class="photo" role="img" aria-label="Indoor sports hall with rows of blue and yellow stadium seats facing a timber court" style="position:absolute;left:0;right:0;bottom:0;height:185px;background:linear-gradient(180deg,#ffffff 0%,#b9c0cb 25%,#7d879a 45%,#c49a5e 55%,#2c4ea8 72%,#e2a91f 88%,#c98a17 100%)"></div>
</section>

<section class="page" style="left:200px;top:540px">
  <div style="position:absolute;left:30px;right:30px;top:34px;display:grid;grid-template-columns:1fr 1fr;gap:12px 18px">
    <div class="photo ph-court" role="img" aria-label="Stadium with timber basketball court and tiered seating" style="height:108px"><span class="tag">Ridgeway Stadium</span></div>
    <div class="photo ph-blue" role="img" aria-label="Dance studio with blue retractable bench seating" style="height:108px"><span class="tag">Tempo – Dance Studio</span></div>
    <div class="photo ph-teal" role="img" aria-label="Esports arena with green lighting and seating" style="height:108px"><span class="tag">Harbour Arena</span></div>
    <div class="photo ph-dark" role="img" aria-label="Sports hall with retractable seating under roof trusses" style="height:108px"><span class="tag">Kestrel SC</span></div>
  </div>
  <div class="photo ph-mixed" role="img" aria-label="Sports centre with red and grey tiered seating" style="position:absolute;left:30px;right:30px;top:284px;height:118px"><span class="tag" style="text-align:center">Greenvale Sports Centre</span></div>
</section>

<section class="page" style="left:618px;top:540px">
  <div class="section-head"><span class="band">Sports Seating</span></div>
  <div class="rows" style="top:60px">
    <div class="row" style="height:84px">
      <div class="photo ph-blue" role="img" aria-label="Blue bench seat on timber platform" style="height:66px"></div>
      <div class="copy"><div class="item-title">Baseline</div><p class="body-text">The Baseline range applies innovative design to traditional linear telescopic seating. It provides a continuous comfort-curve style bench seat with a waterfall front edge to provide enhanced spectator comfort.</p></div>
    </div>
    <div class="row shade" style="height:92px">
      <div class="copy"><div class="item-title">Baseline with<br>Backrest</div><p class="body-text">A backrest can be added to the Baseline to increase the comfort level of the spectators. The backrest folds down to allow the seat rows to retract.</p></div>
      <div class="photo ph-red" role="img" aria-label="Rows of red bench seats with backrests" style="height:66px"></div>
    </div>
    <div class="row" style="height:92px">
      <div class="photo ph-teal" role="img" aria-label="Rows of green tip-up seats" style="height:66px"></div>
      <div class="copy"><div class="item-title">Contour</div><p class="body-text">The Contour range suits both stadiums and arena environments. The unit comprises a seat and backrest moulded from premium grade polypropylene co-polymer. Comfort is superior to any alternative and allows spectators to enjoy long periods of time.</p></div>
    </div>
    <div class="row shade" style="height:90px">
      <div class="copy"><div class="item-title">Contour Padded</div><p class="body-text">The Contour Padded maximises optimal comfort for the seat space. The padded options are finished with marine grade vinyl for indoor and outdoor use or high quality fabric for indoor use only.</p></div>
      <div class="photo ph-red" role="img" aria-label="Padded red stadium seat" style="height:66px"></div>
    </div>
  </div>
</section>

<section class="page" style="left:200px;top:1030px">
  <div class="section-head"><span class="band">Retractable Systems</span></div>
  <div class="rows" style="top:58px">
    <div class="row" style="height:118px;align-items:flex-start;flex-wrap:wrap;row-gap:8px">
      <div class="photo ph-red" role="img" aria-label="Wall attached retractable red seating" style="height:54px"><span class="tag">Wall Attached</span></div>
      <div class="copy"><p class="body-text">Our most popular telescopic gym seating solution. These retractable wall attached systems are supplied in 3 to 30 tier banks, are extremely adaptable and efficiently recover floor space, allowing you to easily get the most out of your facility at all times.</p></div>
      <div class="copy" style="flex:none;width:128px"><p class="body-text">This system utilises a pocket in the wall to house the seating platform when closed. The ends may or may not be exposed, and the bleacher is hidden from view.</p></div>
      <div class="photo ph-dark" role="img" aria-label="Recessed retractable seating closed in wall" style="height:48px;margin-left:auto"><span class="tag">Recessed</span></div>
    </div>
    <div class="row shade" style="height:72px">
      <div class="photo ph-court" role="img" aria-label="Travelling retractable seating unit" style="height:54px"><span class="tag">Traveling</span></div>
      <div class="copy"><p class="body-text">A hybrid of recessed and portable seating banks, travelling units use integral power to drive the entire bank from one setup position to another. Setup time is greatly reduced compared to individual portable sections.</p></div>
    </div>
    <div class="row" style="height:68px">
      <div class="copy"><p class="body-text">With a heftier rear column that is permanently secured to the floor, these bleachers provide design flexibility for buildings that cannot support wall loading.</p></div>
      <div class="photo ph-red" role="img" aria-label="Freestanding red retractable seating" style="height:50px"><span class="tag">Freestanding</span></div>
    </div>
    <div class="row shade" style="height:64px">
      <div class="photo ph-dark" role="img" aria-label="Portable seating sections in a hall" style="height:50px"><span class="tag">Portable</span></div>
      <div class="copy"><p class="body-text">These seating platform sections allow you to easily move and store bleachers where you want them. Create any number of custom layouts for different events, with locking floor pedals for safety.</p></div>
    </div>
  </div>
</section>

<section class="page" style="left:618px;top:1030px">
  <div class="section-head"><span class="band">Theatre and Auditorium Seating</span></div>
  <div class="rows" style="top:56px">
    <div class="row" style="height:62px"><div class="photo ph-blue" role="img" aria-label="Blue tiered bench seating" style="height:54px"><span class="tag">Tier Bench</span></div><div class="copy"><p class="body-text">Tier Bench is a premium bench that features a generous seat base and a full height backrest, making it the ideal choice for studio theatres and performance spaces with timber or veneer options.</p></div></div>
    <div class="row shade" style="height:62px"><div class="copy"><p class="body-text">The Contour chair is a versatile, durable and cost-effective option. The modern design incorporates a rail-based attachment enabling flexible seating layouts.</p></div><div class="photo ph-gold" role="img" aria-label="Yellow and grey fabric theatre seats" style="height:54px"><span class="tag">Contour Fabric</span></div></div>
    <div class="row" style="height:62px"><div class="photo ph-blue" role="img" aria-label="Slim profile theatre chairs" style="height:54px"><span class="tag">Vista</span></div><div class="copy"><p class="body-text">The Vista chair features a refined design, slim closed profile and exceptional levels of detailing, developed for use in theatre and performing arts venues.</p></div></div>
    <div class="row shade" style="height:62px"><div class="copy"><p class="body-text">A new generation of theatre seating featuring a traditional auditorium chair, distinguished by classic design and the flexibility to create custom solutions.</p></div><div class="photo ph-grey" role="img" aria-label="Grey upholstered auditorium chairs" style="height:54px"><span class="tag">Quadra</span></div></div>
    <div class="row" style="height:62px"><div class="photo" role="img" aria-label="Purple luxury lounge seat" style="height:54px;background:linear-gradient(160deg,#2a1f5a,#6a4fb8,#c9c0e8)"><span class="tag">Orbit Lux</span></div><div class="copy"><p class="body-text">The Orbit Lux chair is a luxurious chair featuring contoured seat and backrests for comfort and aesthetics, available in varying widths.</p></div></div>
  </div>
</section>

<section class="page" style="left:200px;top:1520px">
  <div class="section-head"><span class="band">Loose Seats</span></div>
  <div class="rows" style="top:62px">
    <div class="row shade" style="height:108px"><div class="photo" role="img" aria-label="Two grey stacking chairs with metal frames" style="height:82px;background:linear-gradient(160deg,#f6f6f6,#c9c9c9,#8c8c8c)"></div><div class="copy"><div class="item-title">Stakka</div><p class="body-text">A stacking chair comprising of a one piece moulded polypropylene gas injected shell and a durable steel rod frame finished in chrome as standard. Also available with optional upholstered seat and backrest pads in a range of fabrics.</p></div></div>
    <div class="row" style="height:118px"><div class="copy"><div class="item-title">Stacking Quadra</div><p class="body-text">Our Stacking Quadra combines the convenience and flexibility of traditional portable stacking chairs with the style and comfort you expect in an upholstered auditorium chair. It maintains your room's aesthetic while providing the ability to accommodate ever-changing demand, with an optional transport cart for easy storage.</p></div><div class="photo ph-red" role="img" aria-label="Red upholstered stacking auditorium chairs" style="height:82px"></div></div>
    <div class="row shade" style="height:120px"><div class="photo ph-dark" role="img" aria-label="Hall with rows of loose flat floor seats" style="height:82px"></div><div class="copy"><div class="item-title">Lattice</div><p class="body-text">Lattice flat floor seating system allows any choice of seat tipping model to be arranged in row formation. Increased seating capacity with automatic tipping seat, safe to assemble by one person faster than conventional folding or stacking chairs, and easily stored.</p></div></div>
  </div>
</section>

<section class="page" style="left:618px;top:1520px">
  <div class="section-head"><span class="band">Fixed Seating</span></div>
  <div class="rows" style="top:56px">
    <div class="row" style="height:70px"><div class="photo ph-red" role="img" aria-label="Red bleacher seating" style="height:58px"><span class="tag">Bleacher</span></div><div class="copy"><p class="body-text">Bleacher seat provides an affordable renovation that will extend the life of your original investment as well as delivering fans a comfortable spectator experience.</p></div></div>
    <div class="row shade" style="height:70px"><div class="copy"><p class="body-text">The Contour range is applicable to both stadiums and arena environments, with a seat and backrest moulded from premium grade polypropylene.</p></div><div class="photo ph-blue" role="img" aria-label="Blue fixed stadium seats" style="height:58px"><span class="tag">Contour</span></div></div>
    <div class="row" style="height:70px"><div class="photo ph-teal" role="img" aria-label="Low height tread mounted seats" style="height:58px"><span class="tag">Contour – Tread Mount – Low Height</span></div><div class="copy"><p class="body-text">The tread mounted rail allows the use of the popular Contour seat to be used on a timber or concrete platform, perfect for existing structures.</p></div></div>
    <div class="row shade" style="height:74px"><div class="copy"><p class="body-text">Lumen is a comprehensive range of upholstered tipping seats for arena fixed and telescopic applications, with a choice of plastic panels, fabric or vinyl for performing arts and stadiums.</p></div><div class="photo ph-blue" role="img" aria-label="Blue upholstered arena seats" style="height:58px"><span class="tag">Lumen</span></div></div>
    <div class="row" style="height:78px"><div class="photo ph-red" role="img" aria-label="Red theatre with fixed seating" style="height:58px"><span class="tag">Quadra</span></div><div class="copy"><p class="body-text">As elegant as it is functional, the designer series seat style combines rich wood or laminate tones and plush upholstered seats to offer the ultimate in fixed spectator seating with a stunning effect.</p></div></div>
  </div>
</section>

<section class="page" style="left:200px;top:2010px">
  <div class="photo" role="img" aria-label="Indoor basketball stadium with blue seating around a timber court" style="position:absolute;inset:0;background:linear-gradient(180deg,#111418 0%,#3b3f47 22%,#2a3e7e 42%,#b67c45 58%,#e0a868 80%,#8a8f98 100%)"></div>
</section>

<section class="page" style="left:618px;top:2010px">
  <div class="section-head"><span class="band">Accessories</span></div>
  <div class="grid2" style="top:50px;row-gap:6px">
    <div class="cell"><div class="photo ph-dark" role="img" aria-label="LED aisle lights on seating steps" style="height:52px"><span class="tag">LED Aisle Lights</span></div><p class="body-text">LED side lights provide gentle illumination needed to guide patrons to their seat during events.</p></div>
    <div class="cell"><div class="photo ph-red" role="img" aria-label="Glow aisle lights" style="height:52px"><span class="tag">Lumaglow Aisle Lights</span></div><p class="body-text">Lumaglow lights provide lighting to the aisle steps when rooms become dark, without power use.</p></div>
    <div class="cell"><div class="photo ph-court" role="img" aria-label="Timber fascia panels on closed seating" style="height:52px"><span class="tag">Fascia Panels</span></div><p class="body-text">Laminate panels which hide the seating platform in the closed position, blending into the room.</p></div>
    <div class="cell"><div class="photo ph-grey" role="img" aria-label="Side curtains on bleacher" style="height:52px"><span class="tag">Side Curtains</span></div><p class="body-text">Prevent unauthorised access to the underside of the bleacher, reducing potential injury.</p></div>
    <div class="cell"><div class="photo ph-dark" role="img" aria-label="Media platform on seating" style="height:52px"><span class="tag">Media Platforms</span></div><p class="body-text">With a fixed removable media platform you gain a stable secure area for cameras and broadcast.</p></div>
    <div class="cell"><div class="photo ph-grey" role="img" aria-label="Tech deck on seating platform" style="height:52px"><span class="tag">Tech Decks</span></div><p class="body-text">Tech deck is a versatile demountable modular decking system configured to suit fixed seating.</p></div>
    <div class="cell"><div class="photo ph-blue" role="img" aria-label="Aisle hand rails on blue seating" style="height:52px"><span class="tag">Aisle Hand Rails</span></div><p class="body-text">Handrail design ensures your patrons will always find a secure handhold on the aisle steps.</p></div>
    <div class="cell"><div class="photo ph-grey" role="img" aria-label="Writing tablets on seats" style="height:52px"><span class="tag">Writing Tablets</span></div><p class="body-text">Tablets have been designed so they can be used in fixed and telescopic applications.</p></div>
  </div>
</section>

<section class="page" style="left:50px;top:2500px">
  <div class="section-head"><span class="band">Accessories</span></div>
  <div class="grid2" style="top:50px;row-gap:6px">
    <div class="cell"><div class="photo ph-red" role="img" aria-label="Red seats with arm rests" style="height:50px"><span class="tag">Arm Rests</span></div><p class="body-text">Arm rests provide further comfort for the spectator and can be supplied in various options.</p></div>
    <div class="cell"><div class="photo ph-grey" role="img" aria-label="USB power outlet in seat" style="height:50px"><span class="tag">USB / Power Outlets</span></div><p class="body-text">USB and power outlets can be fitted to the retractable platform for spectator devices.</p></div>
    <div class="cell"><div class="photo ph-teal" role="img" aria-label="Seating with printed arena graphics" style="height:50px"><span class="tag">Logos and Graphics</span></div><p class="body-text">Logos and graphics can be added to seats, fascia panels and curtains to brand your venue.</p></div>
    <div class="cell"><div class="photo ph-dark" role="img" aria-label="Row zero floor level seating" style="height:50px"><span class="tag">Row 0</span></div><p class="body-text">Row 0 seating gives floor level seating on the front of any retractable platform.</p></div>
  </div>
  <div class="subhead" style="position:absolute;left:30px;top:262px">Deck Options</div>
  <div class="grid2" style="top:280px;row-gap:4px">
    <div class="cell"><div class="photo" role="img" aria-label="Pink seats on timber deck" style="height:38px;background:linear-gradient(180deg,#e13b73,#c04a7a,#a07050)"></div><div class="deck-name">Wood –</div><p class="body-text" style="margin-top:1px">Clear coated pine decks are a durable option.</p></div>
    <div class="cell"><div class="photo ph-teal" role="img" aria-label="Polydeck flooring under seats" style="height:38px"></div><div class="deck-name">Polydeck –</div><p class="body-text" style="margin-top:1px">A textured plastic veneer over plywood.</p></div>
    <div class="cell"><div class="photo ph-grey" role="img" aria-label="Carpeted deck under seats" style="height:38px"></div><div class="deck-name">Carpet –</div><p class="body-text" style="margin-top:1px">Marine grade durable water resistant carpet.</p></div>
    <div class="cell"><div class="deck-name" style="margin-top:0">Aluminium –</div><p class="body-text" style="margin-top:1px">An extruded plank that is fully non-combustible.</p><div class="deck-name">Vinyl –</div><p class="body-text" style="margin-top:1px">Matched to the other surfaces in the venue.</p></div>
  </div>
</section>

<section class="page" style="left:428px;top:2500px">
  <div class="venues">
    <div class="venue"><span class="name">Westbrook Events Centre</span><span class="lead"></span><span class="qty">Retractable Seating – 2,582 &nbsp;Fixed Seating – 340</span></div>
    <div class="venue"><span class="name">Ridgeway Stadium</span><span class="lead"></span><span class="qty">Retractable Seating – 2,484 &nbsp;Fixed Seating – 1,177</span></div>
    <div class="venue"><span class="name">Copperleaf Stadium</span><span class="lead"></span><span class="qty">Retractable Seating – 1,614</span></div>
    <div class="venue"><span class="name">Dunmore MSC</span><span class="lead"></span><span class="qty">Fixed seating – 295</span></div>
    <div class="venue"><span class="name">Greenvale Sports Centre</span><span class="lead"></span><span class="qty">Retractable seating – 629</span></div>
    <div class="venue"><span class="name">Oakridge CC</span><span class="lead"></span><span class="qty">Retractable seating – 478</span></div>
    <div class="venue"><span class="name">Pinehurst College</span><span class="lead"></span><span class="qty">Retractable seating – 339</span></div>
    <div class="venue"><span class="name">Harbour Arena</span><span class="lead"></span><span class="qty">Retractable seating – 204</span></div>
    <div class="venue"><span class="name">Eastgate Arena</span><span class="lead"></span><span class="qty">Retractable seating – 156</span></div>
    <div class="venue"><span class="name">Hillside Lutheran College</span><span class="lead"></span><span class="qty">Retractable seating – 153</span></div>
    <div class="venue"><span class="name">Marlow Rec Arena</span><span class="lead"></span><span class="qty">Retractable seating – 428</span></div>
    <div class="venue"><span class="name">Jasper Park Rec</span><span class="lead"></span><span class="qty">Retractable seating – 1,002</span></div>
    <div class="venue"><span class="name">Lakeview Rec Hub</span><span class="lead"></span><span class="qty">Retractable seating – 863 &nbsp;Fixed Seating – 328</span></div>
    <div class="venue"><span class="name">Tallis PS</span><span class="lead"></span><span class="qty">Retractable seating – 220</span></div>
    <div class="venue"><span class="name">Redgum Basketball</span><span class="lead"></span><span class="qty">Retractable seating – 216</span></div>
    <div class="venue"><span class="name">Norfield Courts</span><span class="lead"></span><span class="qty">Fixed seating – 3,460</span></div>
    <div class="venue"><span class="name">Merriden</span><span class="lead"></span><span class="qty">Retractable seating – 84</span></div>
    <div class="venue"><span class="name">Kestrel SC</span><span class="lead"></span><span class="qty">Retractable seating – 1,100</span></div>
    <div class="venue"><span class="name">Brookfield Grammar</span><span class="lead"></span><span class="qty">Retractable seating – 590 &nbsp;Fixed seating – 47</span></div>
    <div class="venue"><span class="name">Sandy Creek Rec</span><span class="lead"></span><span class="qty">Fixed seating – 54</span></div>
    <div class="venue"><span class="name">Bayside High School</span><span class="lead"></span><span class="qty">Retractable seating – 306</span></div>
    <div class="venue"><span class="name">St Anselm's Stadium</span><span class="lead"></span><span class="qty">Retractable seating – 194</span></div>
    <div class="venue"><span class="name">Thornbury Sports Stadium</span><span class="lead"></span><span class="qty">Retractable seating – 2,500</span></div>
    <div class="venue"><span class="name">Willowdale SC</span><span class="lead"></span><span class="qty">Retractable seating – 416</span></div>
    <div class="venue"><span class="name">Ashgrove High School</span><span class="lead"></span><span class="qty">Retractable seating – 360</span></div>
    <div class="venue"><span class="name">Fernleigh Secondary College</span><span class="lead"></span><span class="qty">Retractable seating – 224</span></div>
    <div class="venue"><span class="name">Wattle Senior Secondary College</span><span class="lead"></span><span class="qty">Retractable seating – 725 &nbsp;Loose seats – 400</span></div>
  </div>
</section>

<section class="page dark" style="left:806px;top:2500px">
  <div class="brand-mark" style="position:absolute;top:58px;left:0;right:0">
    <span class="brand-dot" style="width:10px;height:10px"></span>
    <span class="brand" style="font-size:14px">BRIM CHAIRWORKS</span>
  </div>
  <div class="contact" style="top:130px;font-size:11px;font-weight:700">Contact Us</div>
  <svg style="position:absolute;left:159px;top:154px" width="12" height="12" viewBox="0 0 24 24"><path d="M6.6 10.8a15.1 15.1 0 0 0 6.6 6.6l2.2-2.2c.3-.3.7-.4 1-.2 1.1.4 2.3.6 3.6.6.6 0 1 .4 1 1V20c0 .6-.4 1-1 1A17 17 0 0 1 3 4c0-.6.4-1 1-1h3.5c.6 0 1 .4 1 1 0 1.3.2 2.5.6 3.6.1.3 0 .7-.2 1z" fill="#e3202a"/></svg>
  <div class="contact" style="top:172px;font-size:17px;font-weight:700">1300 274 600</div>
  <span class="dots" style="left:18px;top:182px"></span><span class="dots" style="right:18px;top:182px"></span>
  <svg style="position:absolute;left:159px;top:208px" width="12" height="10" viewBox="0 0 24 18"><rect x="1" y="1" width="22" height="16" fill="none" stroke="#e3202a" stroke-width="2"/><path d="M1 1l11 9 11-9" fill="none" stroke="#e3202a" stroke-width="2"/></svg>
  <div class="contact" style="top:222px;font-size:7px">info@brimchairworks.com.au</div>
  <div class="contact" style="top:278px;font-size:7.5px;line-height:1.5">Alternative Contact:<br>Daniel Marsh</div>
  <span class="dots" style="left:18px;top:322px"></span><span class="dots" style="right:18px;top:322px"></span>
  <svg style="position:absolute;left:159px;top:328px" width="12" height="10" viewBox="0 0 24 18"><rect x="1" y="1" width="22" height="16" fill="none" stroke="#e3202a" stroke-width="2"/><path d="M1 1l11 9 11-9" fill="none" stroke="#e3202a" stroke-width="2"/></svg>
  <div class="contact" style="top:342px;font-size:7px">daniel@brimchairworks.com.au</div>
  <svg style="position:absolute;left:160px;top:360px" width="10" height="13" viewBox="0 0 20 26"><path d="M10 1a8 8 0 0 0-8 8c0 6 8 16 8 16s8-10 8-16a8 8 0 0 0-8-8z" fill="none" stroke="#e3202a" stroke-width="2"/><circle cx="10" cy="9" r="3" fill="#e3202a"/></svg>
  <div class="contact" style="top:378px;font-size:7px">18 Lorimer St Kenwick, Vic 3000</div>
</section>

</body>
</html>
```